Succession & Estate Planning firm needs a double-sided one page client handout

We need a client hand-out that highlights the top 10 Reasons to get a Pension Plan. It will need the 10 reasons as headings, with a short description of each reason (attached Word doc). It should communicate that a Pension Plan is flexible and provides security. Our usual client is a business owner/medical professional/entrepreneur. Have a look at our website for more info about our business www.quorvane.ca Our logo colours are 83c242, 3b3839, d5d5d5 We like clean, modern, info-graphics, not too cluttered, not too loudWe would like the ability to update the text/content ourselves, in the future.

```html
<!DOCTYPE html>
<html lang="en">
<head>
<meta charset="utf-8">
<title>Quorvane – Top 10 Benefits of a Family Pension Plan</title>
<link href="https://fonts.googleapis.com/css2?family=Bebas+Neue&family=Oswald:wght@500;600&family=Montserrat:wght@300;400;500;600&display=swap" rel="stylesheet">
<style>
  :root {
    --green: #83c242;
    --charcoal: #3b3839;
    --silver: #d5d5d5;
    --row-grey: #e4e4e4;
    --icon-grey: #8d8d8d;
    --paper: #ffffff;
    --backdrop: #ecebe8;
    --body-text: #3b3839;
  }
  * { box-sizing: border-box; margin: 0; padding: 0; }
  html, body { width: 1200px; height: 1200px; overflow: hidden; }
  body {
    background: var(--backdrop);
    font-family: "Montserrat", sans-serif;
    color: var(--body-text);
    position: relative;
  }
  .sheet {
    position: absolute;
    top: 218px;
    width: 540px;
    height: 764px;
    background: var(--paper);
    box-shadow: 0 2px 10px rgba(0,0,0,0.15);
    overflow: hidden;
  }
  .sheet--front { left: 45px; }
  .sheet--back { left: 615px; }

  /* Front side */
  .hero {
    position: absolute; left: 0; top: 0; width: 540px; height: 504px;
    background: linear-gradient(180deg, #f4f6f7 0%, #eef2ee 22%, #dfe9c9 42%, #a9c86a 60%, #7f9a3c 72%, #6b5a3a 86%, #3e3124 100%);
  }
  .brand {
    position: absolute; left: 0; right: 0; top: 72px;
    display: flex; align-items: center; justify-content: center; gap: 12px;
  }
  .brand__mark {
    width: 18px; height: 18px; border-radius: 50%; background: var(--charcoal);
  }
  .brand__name {
    font-family: "Montserrat", sans-serif;
    font-weight: 500;
    font-size: 38px;
    letter-spacing: 1px;
    color: var(--charcoal);
  }
  .title-band {
    position: absolute; left: 0; top: 504px; width: 540px; height: 50px;
    background: var(--green);
    color: #fff;
    font-family: "Bebas Neue", sans-serif;
    font-weight: 400;
    font-size: 33px;
    line-height: 50px;
    text-align: center;
    letter-spacing: 0.3px;
  }
  .intro {
    position: absolute; left: 26px; right: 26px; top: 566px;
  }
  .intro__heading {
    font-size: 22px; font-weight: 500; text-align: center; color: #2b2829;
    margin-bottom: 10px;
  }
  .intro__body {
    font-size: 9.6px; line-height: 12.2px; text-align: justify; color: #333;
  }
  .front-footer {
    position: absolute; left: 0; bottom: 0; width: 540px; height: 48px;
    background: var(--charcoal);
  }
  .front-footer__address {
    position: absolute; left: 26px; top: 10px;
    color: #fff; font-size: 10.5px; font-weight: 500; line-height: 13px;
    display: flex; gap: 6px;
  }
  .front-footer__panel {
    position: absolute; left: 238px; top: 4px; right: 4px; height: 36px;
    background: var(--green);
    clip-path: polygon(0 0, 100% 0, 100% 100%, 22px 100%);
    display: flex; align-items: center; gap: 16px; padding-left: 30px;
    color: #fff; font-size: 10.5px; font-weight: 500;
  }
  .contact { display: flex; align-items: center; gap: 5px; }

  /* Back side */
  .reasons-title {
    position: absolute; left: 25px; top: 20px;
    font-family: "Oswald", sans-serif; font-weight: 600;
    font-size: 20px; letter-spacing: -0.2px; white-space: nowrap;
    color: var(--charcoal);
  }
  .reasons-title span { color: var(--green); }
  .reasons { position: absolute; left: 25px; top: 57px; width: 480px; list-style: none; }
  .reason {
    position: relative; height: 54px; margin-bottom: 11px;
  }
  .reason__bar {
    position: absolute; left: 0; top: 0; width: 394px; height: 54px;
    background: var(--row-grey);
    clip-path: polygon(0 0, 100% 0, 100% 42%, 96.5% 50%, 100% 58%, 100% 100%, 0 100%);
  }
  .reason__num {
    position: absolute; left: 0; top: 14px; width: 72px; height: 40px;
    background: var(--green);
    clip-path: polygon(0 0, 58px 0, 72px 100%, 0 100%);
    color: #fff; font-size: 24px; font-weight: 500;
    padding-left: 22px; line-height: 40px;
  }
  .reason__text { position: absolute; left: 83px; top: 8px; width: 302px; }
  .reason__heading { font-size: 9.3px; font-weight: 600; color: #2b2829; margin-bottom: 3px; }
  .reason__desc { font-size: 6.9px; line-height: 8.6px; text-align: justify; color: #444; }
  .reason__icon {
    position: absolute; left: 402px; top: 0; width: 84px; height: 54px;
    background: var(--icon-grey);
    display: flex; align-items: center; justify-content: center;
  }
  .reason__icon svg { width: 34px; height: 34px; stroke: #fff; fill: none; stroke-width: 2; stroke-linecap: round; stroke-linejoin: round; }
  .back-footer {
    position: absolute; left: 0; bottom: 0; width: 540px; height: 46px;
    background: var(--charcoal);
  }
  .back-footer__phone {
    position: absolute; left: 28px; top: 13px; color: #fff;
    font-size: 15px; font-weight: 500; display: flex; align-items: center; gap: 8px;
  }
  .back-footer__web {
    position: absolute; left: 193px; top: 0; right: 0; height: 30px;
    background: var(--green);
    clip-path: polygon(0 0, 100% 0, 100% 100%, 12px 100%);
    color: #fff; font-size: 12px; letter-spacing: 5px; text-align: center; line-height: 30px;
  }
</style>
</head>
<body>

<section class="sheet sheet--front">
  <div class="hero" role="img" aria-label="Young green seedlings growing out of stacks of gold coins set in soil, soft sunny field behind"></div>
  <div class="brand">
    <span class="brand__mark"></span>
    <span class="brand__name">Quorvane</span>
  </div>
  <h1 class="title-band">Top 10 Benefits of a Family Pension Plan</h1>
  <div class="intro">
    <h2 class="intro__heading">Succession &amp; Estate Planning</h2>
    <p class="intro__body">Succession and estate planning can often seem like a puzzle. Due to the numerous complex issues that are intertwined in succession and estate planning, beginning the process can be a daunting task. That is why we are here to help. We will walk with you through each piece of the puzzle and see how it will all work together in your unique situation. By working collaboratively with our client's team of professional advisors, we are passionate about helping our clients clarify their goals for estate, succession and philanthropy planning, to give them the confidence to move forward, and take action in making these dreams a reality.</p>
  </div>
  <footer class="front-footer">
    <div class="front-footer__address">
      <svg width="12" height="11" viewBox="0 0 12 11"><path d="M6 0 L12 5 L10.5 5 L10.5 11 L7.5 11 L7.5 7 L4.5 7 L4.5 11 L1.5 11 L1.5 5 L0 5 Z" fill="#83c242"/></svg>
      <div>412 – 88 Elm Avenue<br>Saskatoon, Saskatchewan, S7K 2R4</div>
    </div>
    <div class="front-footer__panel">
      <span class="contact">
        <svg width="12" height="12" viewBox="0 0 24 24" fill="none" stroke="#fff" stroke-width="2.2"><path d="M5 3h4l2 5-3 2a11 11 0 0 0 6 6l2-3 5 2v4a2 2 0 0 1-2 2A17 17 0 0 1 3 5a2 2 0 0 1 2-2z"/></svg>
        (306) 555-0142
      </span>
      <span class="contact">
        <svg width="12" height="12" viewBox="0 0 24 24" fill="none" stroke="#fff" stroke-width="2"><circle cx="12" cy="12" r="10"/><path d="M2 12h20M12 2c3 3 3 17 0 20M12 2c-3 3-3 17 0 20"/></svg>
        www.quorvane.ca
      </span>
    </div>
  </footer>
</section>

<section class="sheet sheet--back">
  <h2 class="reasons-title">TOP 10 REASONS <span>Why an FPP Serves Your Family Enterprise</span></h2>
  <ol class="reasons">
    <li class="reason">
      <div class="reason__bar"></div><div class="reason__num">1</div>
      <div class="reason__text"><h3 class="reason__heading">Create Significant Deductions</h3>
        <p class="reason__desc">The FPP creates significant tax deductions, which can be used to keep the business under the small business rate or applied to the high rate, a bigger bang for the buck.</p></div>
      <div class="reason__icon"><svg viewBox="0 0 24 24"><rect x="3" y="5" width="15" height="9"/><circle cx="10.5" cy="9.5" r="2"/><circle cx="18" cy="17" r="4"/><path d="M18 15v4"/></svg></div>
    </li>
    <li class="reason">
      <div class="reason__bar"></div><div class="reason__num">2</div>
      <div class="reason__text"><h3 class="reason__heading">Deliberate, Planned, Future Income</h3>
        <p class="reason__desc">An income for beyond the last day at the office.</p></div>
      <div class="reason__icon"><svg viewBox="0 0 24 24"><circle cx="13" cy="7" r="4"/><path d="M13 5v4"/><path d="M3 17h5l4 2 7-4"/><path d="M3 21h9l9-5"/></svg></div>
    </li>
    <li class="reason">
      <div class="reason__bar"></div><div class="reason__num">3</div>
      <div class="reason__text"><h3 class="reason__heading">Past Buy Back</h3>
        <p class="reason__desc">Most owners invest, first, in the business. The FPP offers the ability to go back and recover lost years when they did not buy RRSPs...and pass the tax savings onto their company.</p></div>
      <div class="reason__icon"><svg viewBox="0 0 24 24"><path d="M4 12a8 8 0 1 0 3-6.2"/><path d="M3 3v5h5"/><path d="M12 7v5h4"/></svg></div>
    </li>
    <li class="reason">
      <div class="reason__bar"></div><div class="reason__num">4</div>
      <div class="reason__text"><h3 class="reason__heading">Creditor Proof</h3>
        <p class="reason__desc">All Assets held in an FPP are creditor proof, including RRSPs, &amp; planned pension contributions receive "super-priority" status, which rank above the claims of secured creditors, like major commercial lenders &amp; banks.</p></div>
      <div class="reason__icon"><svg viewBox="0 0 24 24"><path d="M3 11a9 9 0 0 1 18 0z"/><path d="M12 11v8a2 2 0 0 1-4 0"/><circle cx="6" cy="17" r="2.5"/><circle cx="18" cy="17" r="2.5"/></svg></div>
    </li>
    <li class="reason">
      <div class="reason__bar"></div><div class="reason__num">5</div>
      <div class="reason__text"><h3 class="reason__heading">Flexibility</h3>
        <p class="reason__desc">Owners know that cash flows can swing wildly with the business cycle. An FPP offers the flexibility to flip between DB and DC accounts in order to conserve cash, smooth income during volatile years, &amp; recover assets when things improve.</p></div>
      <div class="reason__icon"><svg viewBox="0 0 24 24"><path d="M12 22V3M9 6l3-3 3 3"/><path d="M12 13 4 9M4 9v3M4 9h3"/><path d="M12 13l8-4M20 9v3M20 9h-3"/></svg></div>
    </li>
    <li class="reason">
      <div class="reason__bar"></div><div class="reason__num">6</div>
      <div class="reason__text"><h3 class="reason__heading">Preserve the Lifetime Capital Gains Exemption</h3>
        <p class="reason__desc">Create $1.6 Million++ of Tax Free Capital Gains. The significant deductions created in an FPP can be used to purify a corporation with passive assets, which can help preserve the shareholders' lifetime capital gains exemption.</p></div>
      <div class="reason__icon"><svg viewBox="0 0 24 24"><path d="M10 8V6M13 8V4M16 8V3M19 8V2"/><rect x="4" y="11" width="16" height="9"/><circle cx="12" cy="15.5" r="2.5"/></svg></div>
    </li>
    <li class="reason">
      <div class="reason__bar"></div><div class="reason__num">7</div>
      <div class="reason__text"><h3 class="reason__heading">Intergenerational Wealth Transfer</h3>
        <p class="reason__desc">Unlike RRSPs that eventually trigger a taxable disposition upon death, an FPP has the ability to pass, tax deferred, to the next generation of family business owners.</p></div>
      <div class="reason__icon"><svg viewBox="0 0 24 24"><rect x="3" y="8" width="18" height="9"/><circle cx="12" cy="12.5" r="2.5"/><path d="M8 4h9l-2-2M16 21H7l2 2"/></svg></div>
    </li>
    <li class="reason">
      <div class="reason__bar"></div><div class="reason__num">8</div>
      <div class="reason__text"><h3 class="reason__heading">All Ages</h3>
        <p class="reason__desc">An FPP can benefit all entrepreneurs between ages 18-71.</p></div>
      <div class="reason__icon"><svg viewBox="0 0 24 24"><circle cx="5" cy="7" r="2"/><path d="M5 11v10"/><circle cx="11" cy="9" r="1.6"/><path d="M11 12v9"/><circle cx="15" cy="9" r="1.6"/><path d="M15 12v9"/><circle cx="20" cy="7" r="2"/><path d="M20 11v10"/></svg></div>
    </li>
    <li class="reason">
      <div class="reason__bar"></div><div class="reason__num">9</div>
      <div class="reason__text"><h3 class="reason__heading">Conserve the Small Business Deduction</h3>
        <p class="reason__desc">Investment income inside an FPP grows tax exempt and does not create passive income as outlined under the 2018 "Passive Income Measures". Therefore, business owners that redirect corporate resources to fund their pension assets will not jeopardize their low corporate tax rate on profits &amp; in associated companies.</p></div>
      <div class="reason__icon"><svg viewBox="0 0 24 24"><circle cx="13" cy="8" r="6"/><path d="M13 5v6M11 7h4M11 10h4"/><path d="M2 18h5l4 2 7-4"/></svg></div>
    </li>
    <li class="reason">
      <div class="reason__bar"></div><div class="reason__num">10</div>
      <div class="reason__text"><h3 class="reason__heading">Broader Investment Options</h3>
        <p class="reason__desc">An FPP allows entrepreneurs to invest in what they like: real estate, other businesses and/or franchises, private equity, public equity, exempt markets, etc. The possibilities are up to the imagination of the entrepreneur &amp; their advisors.</p></div>
      <div class="reason__icon"><svg viewBox="0 0 24 24"><path d="M4 21v-5M8 21v-7M12 21v-9M16 21v-11M20 21V7"/><path d="M3 13 9 9l4 2 7-7M16 4h4v4"/></svg></div>
    </li>
  </ol>
  <footer class="back-footer">
    <div class="back-footer__phone">
      <svg width="15" height="15" viewBox="0 0 24 24" fill="none" stroke="#fff" stroke-width="2"><path d="M5 3h4l2 5-3 2a11 11 0 0 0 6 6l2-3 5 2v4a2 2 0 0 1-2 2A17 17 0 0 1 3 5a2 2 0 0 1 2-2z"/></svg>
      (306) 555-0142
    </div>
    <div class="back-footer__web">www.quorvane.ca</div>
  </footer>
</section>

</body>
</html>
```